Banner Ad for Resume Services Website

The add is for this web site: www.BrightFolioDesk.com

The site offers 4 different services:

- Resume Writing (by a Certified Professional Resume Writer)
- Resume Posting (posts your resume to 85 job sites)
- Resume Distribution (sends your resume to hundreds of recruiters)
- Resume Online website (created an online resume with a domain name to your name)

Colors to be used are Blue, Yellow, etc... please check the website for inspiration.

Check the web site to learn more.

Target Market(s)

Unemployed, Professionals who want to switch jobs, etc..

Industry/Entity Type

Learn

Requirements
Must have
• We definitely one this to be included on the banner:

"Free Resume Samples"

in order to attract clicks.
Nice to have
• Some of the words we suggest to include on the banner are:

"How Good is Your Resume? Ask a Professional !"

Should not have
• No animation !

Do not place the LOGO on the banner as our LOGO might change in the near future. If you already submitted a banner with the LOGO on it, you can replace it with any other graphic that has a Resume/Jobs/BusinessStaff related theme.

```html
<!DOCTYPE html>
<html lang="en">
<head>
<meta charset="utf-8">
<title>Resume Writing – $99 | BrightFolioDesk</title>
<link href="https://fonts.googleapis.com/css2?family=Open+Sans:wght@400;600;700;800&display=swap" rel="stylesheet">
<style>
  :root {
    --bg-light: #ffffff;
    --bg-edge: #d9d9d9;
    --title: #4a4a4a;
    --text: #585858;
    --tick: #7a7a7a;
    --rule: #8a8a8a;
    --ribbon-top: #f79a2a;
    --ribbon-bottom: #e4670f;
    --wave-light: #b5d2ea;
    --wave-dark: #2a6cab;
    --wave-deep: #1d5a95;
    --accent: #ffc933;
    --on-blue: #ffffff;
  }
  html, body {
    margin: 0;
    padding: 0;
    overflow: hidden;
    background: #ffffff;
  }
  .banner {
    position: relative;
    width: 1200px;
    height: 803px;
    overflow: hidden;
    background: radial-gradient(ellipse 75% 70% at 45% 40%, var(--bg-light) 0%, #f1f1f1 55%, var(--bg-edge) 100%);
    font-family: "Open Sans", Arial, sans-serif;
  }
  .banner-shapes {
    position: absolute;
    inset: 0;
  }
  .service-title {
    position: absolute;
    left: 54px;
    top: 26px;
    margin: 0;
    font-size: 57px;
    font-weight: 800;
    letter-spacing: 0.5px;
    color: var(--title);
    text-transform: uppercase;
  }
  .feature-list {
    position: absolute;
    left: 66px;
    top: 166px;
    margin: 0;
    padding: 0;
    list-style: none;
  }
  .feature-list li {
    display: flex;
    align-items: center;
    height: 85px;
    font-size: 39px;
    color: var(--text);
    white-space: nowrap;
  }
  .feature-list .tick {
    width: 42px;
    height: 42px;
    margin-right: 41px;
    flex: none;
  }
  .price {
    position: absolute;
    left: 1110px;
    top: 92px;
    transform: translate(-50%, -50%) rotate(45deg);
    font-size: 52px;
    font-weight: 700;
    color: #ffffff;
    white-space: nowrap;
  }
  .footer-bar {
    position: absolute;
    left: 66px;
    right: 60px;
    bottom: 18px;
    display: flex;
    align-items: baseline;
    justify-content: space-between;
    color: var(--on-blue);
    white-space: nowrap;
  }
  .free-samples {
    font-size: 34px;
    font-weight: 800;
    color: var(--accent);
    text-transform: uppercase;
    letter-spacing: 0.5px;
  }
  .service-line {
    font-size: 21px;
    font-weight: 600;
    text-align: right;
  }
  .service-line .site {
    display: block;
    font-size: 19px;
    font-weight: 400;
    opacity: 0.9;
  }
</style>
</head>
<body>
<div class="banner">
  <svg class="banner-shapes" width="1200" height="803" viewBox="0 0 1200 803" aria-hidden="true">
    <defs>
      <linearGradient id="title-rule" x1="0" x2="1" y1="0" y2="0">
        <stop offset="0" stop-color="var(--rule)" stop-opacity="0"/>
        <stop offset="0.25" stop-color="var(--rule)" stop-opacity="0.9"/>
        <stop offset="0.7" stop-color="var(--rule)" stop-opacity="0.6"/>
        <stop offset="1" stop-color="var(--rule)" stop-opacity="0"/>
      </linearGradient>
      <linearGradient id="ribbon-fill" x1="0" y1="0" x2="1" y2="1">
        <stop offset="0" stop-color="var(--ribbon-top)"/>
        <stop offset="1" stop-color="var(--ribbon-bottom)"/>
      </linearGradient>
      <linearGradient id="wave-fill" x1="0" y1="0" x2="0" y2="1">
        <stop offset="0" stop-color="var(--wave-dark)"/>
        <stop offset="1" stop-color="var(--wave-deep)"/>
      </linearGradient>
    </defs>
    <rect class="title-rule" x="20" y="118" width="720" height="3" fill="url(#title-rule)"/>
    <polygon class="price-ribbon" points="956,0 1084,0 1200,116 1200,244" fill="url(#ribbon-fill)"/>
    <path class="wave-light" d="M0,600 C320,640 760,680 1200,552 L1200,803 L0,803 Z" fill="var(--wave-light)"/>
    <path class="wave-dark" d="M0,668 C360,745 820,715 1200,618 L1200,803 L0,803 Z" fill="url(#wave-fill)"/>
  </svg>

  <h1 class="service-title">Resume Writing</h1>
  <div class="price">$ 99</div>

  <ul class="feature-list">
    <li><svg class="tick" viewBox="0 0 40 40"><path d="M4,22 L14,34 L36,4" fill="none" stroke="var(--tick)" stroke-width="3" stroke-linecap="round" stroke-linejoin="round"/></svg>Phone Consultation to startyour resume creation</li>
    <li><svg class="tick" viewBox="0 0 40 40"><path d="M4,22 L14,34 L36,4" fill="none" stroke="var(--tick)" stroke-width="3" stroke-linecap="round" stroke-linejoin="round"/></svg>First draft of your resume within 46 hours</li>
    <li><svg class="tick" viewBox="0 0 40 40"><path d="M4,22 L14,34 L36,4" fill="none" stroke="var(--tick)" stroke-width="3" stroke-linecap="round" stroke-linejoin="round"/></svg>Unlimited edits until you’re 100% satisfied</li>
    <li><svg class="tick" viewBox="0 0 40 40"><path d="M4,22 L14,34 L36,4" fill="none" stroke="var(--tick)" stroke-width="3" stroke-linecap="round" stroke-linejoin="round"/></svg>Fully costumized cover letter</li>
    <li><svg class="tick" viewBox="0 0 40 40"><path d="M4,22 L14,34 L36,4" fill="none" stroke="var(--tick)" stroke-width="3" stroke-linecap="round" stroke-linejoin="round"/></svg>Download several career e-bookds FREE</li>
  </ul>

  <div class="footer-bar">
    <span class="free-samples">Free Resume Samples</span>
    <span class="service-line">Writing · Posting · Distribution · Online Resume<span class="site">www.BrightFolioDesk.com</span></span>
  </div>
</div>
</body>
</html>
```